Velvet Dare Age Verification Landing Page

To create a visually appealing design for the landing page of the adult game "Velvet Dare" that confirms the visitor's age.
The design should have a simple and visually appealing look that focuses on two buttons labeled "Yes" and "No". The purpose of the page is to confirm that the visitor is 18 years of age or older before accessing the game's content. Responsive design that works well on desktop and mobile devices. The final output should be delivered in PSD, AI, or Sketch format, along with any necessary images or assets.
I have also attached examples.

```html
<!DOCTYPE html>
<html lang="en">
<head>
<meta charset="utf-8">
<title>Velvet Dare – Age Verification</title>
<link rel="stylesheet" href="https://fonts.googleapis.com/css2?family=Questrial&display=swap">
<style>
  :root {
    --bg-dark: #1c2a31;
    --bg-mid: #33464f;
    --bg-warm: #4a4a42;
    --accent: #cc0d58;
    --accent-dark: #8e1142;
    --text: #ffffff;
  }
  * { margin: 0; padding: 0; box-sizing: border-box; }
  html, body { width: 1200px; height: 547px; overflow: hidden; }
  body {
    font-family: "Questrial", sans-serif;
    color: var(--text);
    position: relative;
    background: var(--bg-dark);
  }
  .backdrop {
    position: absolute; inset: 0;
    background:
      radial-gradient(ellipse 260px 200px at 640px 230px, rgba(90, 84, 70, 0.55), transparent 70%),
      radial-gradient(ellipse 200px 240px at 380px 160px, rgba(70, 66, 58, 0.5), transparent 70%),
      linear-gradient(180deg, var(--bg-mid) 0%, #2c3d45 60%, var(--bg-dark) 100%);
  }
  .music-toggle {
    position: absolute; left: 1061px; top: 19px;
    width: 40px; height: 40px;
    border: 2px solid var(--accent-dark);
    display: flex; align-items: center; justify-content: center;
  }
  .brand {
    position: absolute; left: 0; right: 0; top: 110px;
    text-align: center;
  }
  .brand-circle {
    display: block; margin: 0 auto;
    width: 106px; height: 106px;
    border: 1px solid var(--accent);
    border-radius: 50%;
  }
  .brand-name {
    margin-top: 14px;
    font-size: 46px; line-height: 1;
    color: var(--text);
  }
  .age-gate {
    position: absolute; left: 0; right: 0; top: 330px;
    text-align: center;
  }
  .age-question { font-size: 19px; line-height: 24px; letter-spacing: 0.2px; }
  .age-actions {
    margin-top: 15px;
    display: flex; justify-content: center; gap: 10px;
  }
  .age-btn {
    width: 54px; height: 41px;
    background: var(--accent);
    color: var(--text);
    font-family: inherit; font-size: 17px;
    border: none;
  }
  .remember {
    margin-top: 14px;
    display: flex; justify-content: center; align-items: center; gap: 12px;
    font-size: 13px;
    padding-left: 4px;
  }
  .remember-box { width: 9px; height: 9px; background: var(--text); }
</style>
</head>
<body>
  <div class="backdrop" role="img" aria-label="Blurred photograph of a reclining woman in soft teal light"></div>

  <div class="music-toggle" aria-label="Toggle music">
    <svg width="24" height="26" viewBox="0 0 24 26" fill="var(--text)">
      <path d="M8 3 L21 1 V18.5 A3.5 3 0 1 1 18.6 15.7 V6 L10.4 7.3 V21 A3.5 3 0 1 1 8 18.2 Z"/>
    </svg>
  </div>

  <header class="brand">
    <span class="brand-circle"></span>
    <div class="brand-name">Velvet Dare</div>
  </header>

  <main class="age-gate">
    <p class="age-question">Are You Over 18 years of Age?</p>
    <div class="age-actions">
      <button class="age-btn">Yes</button>
      <button class="age-btn">No</button>
    </div>
    <label class="remember"><span class="remember-box"></span>Remember Me</label>
  </main>
</body>
</html>
```